QUOTE Graphics for Summer Challenge

I would like to put these quotes over one of the pictures attached; For Instagram, use new size: 4:5 (1080 x 1350 pixels). One Quote per picture, and I want the quote to be bold or easy to read as well. I provided a few reference graphics that I really like as examples below.
All of the pictures are attached; you can pick any photo and add one quote to it; but no stock photography
All the quotes are in the attached WORD document

```html
<!DOCTYPE html>
<html lang="en">
<head>
<meta charset="utf-8">
<title>Golden Girl Summer Reset – Quote Post</title>
<link rel="stylesheet" href="https://fonts.googleapis.com/css2?family=Anton&family=Roboto+Condensed:wght@700&display=swap">
<style>
  :root {
    --page-bg: #ece7ea;
    --sky-top: #5a7fbf;
    --sky-mid: #7f9ccc;
    --skin-warm: #8a5a48;
    --sea: #9fb9c9;
    --sand: #f1dfc4;
    --panel-mauve: rgba(104, 80, 108, 0.62);
    --panel-rose: rgba(150, 112, 120, 0.55);
    --text-light: #ffffff;
    --text-shadow: rgba(40, 20, 40, 0.45);
  }

  * { margin: 0; padding: 0; box-sizing: border-box; }

  html, body {
    width: 1200px;
    height: 1000px;
    overflow: hidden;
    background: var(--page-bg);
  }

  .post {
    position: absolute;
    left: 283px;
    top: 105px;
    width: 634px;
    height: 791px;
    overflow: hidden;
  }

  .post__photo {
    position: absolute;
    inset: 0;
    background:
      radial-gradient(ellipse 36% 50% at 38% 55%, var(--skin-warm) 0%, rgba(138, 90, 72, 0.55) 55%, rgba(138, 90, 72, 0) 100%),
      linear-gradient(180deg, var(--sky-top) 0%, var(--sky-mid) 45%, #a9b3c8 66%, var(--sea) 76%, #e6d6c0 88%, var(--sand) 100%);
  }

  .post__panel {
    position: absolute;
    top: 0;
    left: 300px;
    width: 319px;
    height: 100%;
    background: linear-gradient(180deg,
      rgba(90, 127, 191, 0) 0%,
      var(--panel-mauve) 22%,
      var(--panel-mauve) 55%,
      var(--panel-rose) 75%,
      rgba(241, 223, 196, 0.3) 100%);
  }

  .post__copy {
    position: absolute;
    left: 300px;
    width: 312px;
    top: 0;
    height: 100%;
    color: var(--text-light);
    text-align: center;
    text-shadow: 2px 2px 4px var(--text-shadow);
  }

  .headline {
    position: absolute;
    top: 82px;
    left: 0;
    right: 0;
    font-family: "Anton", "Oswald", sans-serif;
    font-weight: 400;
    font-size: 36px;
    line-height: 43px;
    letter-spacing: 0.3px;
    text-transform: uppercase;
  }

  .cta {
    position: absolute;
    top: 386px;
    left: 0;
    right: 0;
    font-family: "Anton", "Oswald", sans-serif;
    text-transform: uppercase;
  }

  .cta__label {
    display: flex;
    justify-content: center;
    align-items: center;
    gap: 5px;
    font-size: 20px;
    line-height: 26px;
    letter-spacing: 0.4px;
  }

  .cta__icon { width: 23px; height: 23px; filter: drop-shadow(1px 1px 2px var(--text-shadow)); }

  .cta__keyword {
    display: inline-block;
    margin-top: 10px;
    width: 151px;
    height: 40px;
    border: 2px solid var(--text-light);
    border-radius: 20px;
    font-size: 28px;
    line-height: 36px;
    box-shadow: 1px 2px 4px var(--text-shadow);
  }

  .program {
    position: absolute;
    top: 508px;
    left: 0;
    right: 0;
    font-family: "Anton", "Oswald", sans-serif;
    font-weight: 400;
    font-size: 36px;
    line-height: 43px;
    text-transform: uppercase;
  }

  .program__rule {
    position: absolute;
    top: 640px;
    left: 28px;
    width: 260px;
    height: 2px;
    background: linear-gradient(90deg, rgba(255,255,255,0) 0%, #fff 15%, #fff 85%, rgba(255,255,255,0) 100%);
  }

  .handle {
    position: absolute;
    top: 679px;
    left: 0;
    right: 0;
    font-family: "Roboto Condensed", "Arial Narrow", sans-serif;
    font-weight: 700;
    font-size: 19px;
    line-height: 22px;
    letter-spacing: 0.3px;
  }
</style>
</head>
<body>
  <article class="post">
    <div class="post__photo" role="img" aria-label="Photo of a smiling woman in sunglasses and a brown bikini standing in a sunlit pool under a clear blue sky"></div>
    <div class="post__panel"></div>

    <div class="post__copy">
      <h1 class="headline">Summer’s here,<br>but your<br>body doesn’t<br>feel ready?<br>You’re not<br>too late.</h1>

      <div class="cta">
        <p class="cta__label">
          <svg class="cta__icon" viewBox="0 0 28 28" aria-hidden="true">
            <path d="M14 3a11 11 0 1 1-6.2 20.1L3 25l1.6-4.6A11 11 0 0 1 14 3z" fill="#fff"/>
          </svg>
          Comment
        </p>
        <span class="cta__keyword">Summer</span>
      </div>

      <h2 class="program">To join<br>the golden girl<br>summer reset</h2>
      <div class="program__rule"></div>

      <p class="handle">@RAEBROOKSWELL</p>
    </div>
  </article>
</body>
</html>
```